Beacon Chillworks business card design

We would like a new design for our business card as we have a new logo.
We need generic business card to give our customers with our office details - with the option of making it individualized for each manager

Target Market(s)

Companies and homeowners

Industry/Entity Type

Air Conditioning

Contact Information for Business Card

We are not sure if we want single or double sided it will depend on the design we choose

Colors
33a6d7
0255a3

Requirements
Must have
• Logo
• phone: (08) 8712 4590
• email: beaconserve@frostmail.example
• website: www.beaconchillworks.example.au
• AU61924
• BLD402613
Nice to have
• Address - Shed 5/218 Kestrel Rd, Marlow Ridge SA 5990

```html
<!DOCTYPE html>
<html lang="en">
<head>
<meta charset="utf-8">
<title>Beacon Chillworks – Business Card</title>
<link rel="stylesheet" href="https://fonts.googleapis.com/css2?family=Arimo:wght@400;700&display=swap">
<style>
  :root {
    --navy: #0255a3;
    --sky: #33a6d7;
    --card: #f7f8f9;
    --ink: #1d1d1f;
    --backdrop: #2b2b2d;
  }
  * { box-sizing: border-box; margin: 0; padding: 0; }
  html, body { width: 1200px; height: 997px; overflow: hidden; }
  body {
    background: var(--backdrop);
    font-family: "Arimo", Arial, sans-serif;
    position: relative;
  }
  .card {
    position: absolute;
    left: 280px;
    width: 640px;
    height: 366px;
    background: var(--card);
    border-radius: 22px;
    overflow: hidden;
  }
  .card--back { top: 90px; }
  .card--front { top: 520px; }

  /* Back face */
  .back-brand {
    position: absolute;
    left: 0; right: 0; top: 120px;
    display: flex; align-items: center; justify-content: center; gap: 14px;
  }
  .brand-dot {
    width: 30px; height: 30px; border-radius: 50%;
    background: var(--sky);
  }
  .back-brand .brand-name {
    font-size: 48px; font-weight: 700; color: var(--navy); letter-spacing: -0.5px;
  }
  .licences {
    position: absolute; left: 0; right: 0; top: 200px;
    display: flex; justify-content: center; gap: 36px;
    font-size: 17px; color: var(--sky); letter-spacing: 0.5px;
  }

  /* Front face */
  .front-brand {
    position: absolute; left: 0; right: 0; top: 48px;
    display: flex; align-items: center; justify-content: center; gap: 10px;
  }
  .front-brand .brand-dot { width: 22px; height: 22px; }
  .front-brand .brand-name {
    font-size: 38px; font-weight: 700; color: var(--navy); letter-spacing: -0.5px;
  }
  .person {
    position: absolute; right: 380px; top: 168px; text-align: right;
  }
  .person__name { font-size: 16px; font-weight: 700; color: var(--navy); letter-spacing: 0.5px; }
  .person__role { font-size: 16px; color: var(--ink); margin-top: 3px; }
  .divider {
    position: absolute; left: 284px; top: 150px; width: 2px; height: 72px;
    background: linear-gradient(to bottom, transparent, #9aa3ae, transparent);
  }
  .contacts {
    position: absolute; left: 304px; top: 150px; list-style: none;
  }
  .contacts li {
    display: flex; align-items: center; gap: 9px;
    font-size: 15px; color: var(--ink); height: 24px; white-space: nowrap;
  }
  .contacts li.web { font-weight: 700; color: var(--navy); }
  .icon { width: 16px; height: 16px; flex: none; }
  .band {
    position: absolute; left: 0; right: 0; top: 258px; height: 28px;
    background: var(--navy); color: #fff;
    font-size: 15px; text-align: center; line-height: 28px; letter-spacing: 0.3px;
  }
  .band-rule {
    position: absolute; left: 0; right: 0; height: 4px; background: var(--navy);
  }
  .band-rule--top { top: 249px; }
  .band-rule--bottom { top: 292px; }
</style>
</head>
<body>

  <section class="card card--back" aria-label="Card back">
    <div class="back-brand">
      <span class="brand-dot"></span>
      <span class="brand-name">Beacon Chillworks</span>
    </div>
    <div class="licences">
      <span>AU61924</span>
      <span>BLD402613</span>
    </div>
  </section>

  <section class="card card--front" aria-label="Card front">
    <div class="front-brand">
      <span class="brand-dot"></span>
      <span class="brand-name">Beacon Chillworks</span>
    </div>

    <div class="person">
      <p class="person__name">MARA ELLISON</p>
      <p class="person__role">Director of Marketing</p>
    </div>

    <div class="divider"></div>

    <ul class="contacts">
      <li>
        <svg class="icon" viewBox="0 0 16 16"><circle cx="8" cy="8" r="8" fill="#0255a3"/><path d="M5 5.5h6v5H5z" fill="none" stroke="#fff" stroke-width="1.2"/><path d="M6.5 8h3" stroke="#fff" stroke-width="1.2"/></svg>
        (08) 8712 4590
      </li>
      <li>
        <svg class="icon" viewBox="0 0 16 16"><circle cx="8" cy="8" r="8" fill="#0255a3"/><rect x="4.5" y="5.5" width="7" height="5" fill="none" stroke="#fff" stroke-width="1"/><path d="M4.5 5.5 8 8.3l3.5-2.8" fill="none" stroke="#fff" stroke-width="1"/></svg>
        beaconserve@frostmail.example
      </li>
      <li class="web">
        <svg class="icon" viewBox="0 0 16 16"><circle cx="8" cy="8" r="8" fill="#0255a3"/><circle cx="8" cy="6.2" r="2" fill="#fff"/><path d="M4.5 12a3.5 3 0 0 1 7 0z" fill="#fff"/></svg>
        www.beaconchillworks.example.au
      </li>
    </ul>

    <div class="band-rule band-rule--top"></div>
    <div class="band">Shed 5/218 Kestrel Rd, Marlow Ridge SA 5990</div>
    <div class="band-rule band-rule--bottom"></div>
  </section>

</body>
</html>
```